Bramblewick Jewellery Limited - designer pearl and silver jewellery

Designer silver jewellery with a twist that 20% of the net profit will be donated to a charity in India to help abused children

The products are designed to make the wearer not only feel good about how good the jewellery looks but to know they are also helping others less fortunate

All the Jewellery is designed by myself Marjorie Toller and made in 925 Hallmarked sterling silver . The hallmarking is carried out by the Corvane Testing office

This is my first website and will need to be suitable for e-commerce
Updates

Target Market(s)

Stylish women with a love of simple and elegant design , not high fashion by timeless simplicity

Number of Pages Required

5+ page

Font styles to use
Sans Serif

Colors
e666a6

Requirements
Must have
• Reference to Sterling silver
• The Pantone ref for my logo background now is white out of 2063
Nice to have
• Fresh and contemporary - Aimed at 25-55 market
• The same consumer would
• Like this product as likes Velisse, Rufus Olbeck but will also appreciate the fact this product is about helping others as well
• The Jewellery is about clean simple lines , elegance , hand made and styled to be timeless
• The products are designed to be casual and elegant and all feature either natural freshwater pearls or semi precious gemstones
• I also would like a page that customers can arrange to book talks about the design and production of the product . I give these talks generally tomladies groups and explain the manufacturing process and what the charity I’m doing supports

```html
<!DOCTYPE html>
<html lang="en">
<head>
<meta charset="utf-8">
<title>Bramblewick Jewellery</title>
<link rel="stylesheet" href="https://fonts.googleapis.com/css2?family=Gelasio:wght@400&family=Arimo:wght@400;700&display=swap">
<style>
  :root {
    --pink: #e666a6;
    --hero-black: #0a0b0d;
    --section-dark: #1b1a17;
    --gold: #e3cc74;
    --white: #ffffff;
    --divider: #f2f2f2;
    --dot-grey: #d9d9d9;
    --serif: "Gelasio", Georgia, serif;
    --sans: "Arimo", Arial, sans-serif;
  }
  * { box-sizing: border-box; margin: 0; padding: 0; }
  html, body { width: 1200px; height: 2350px; overflow: hidden; background: var(--section-dark); }
  a { color: inherit; text-decoration: none; }
  .page { position: relative; width: 1200px; height: 2350px; font-family: var(--sans); color: var(--white); }

  /* Header */
  .site-header { position: absolute; left: 0; top: 0; width: 1200px; height: 110px; background: var(--pink); }
  .main-nav { position: absolute; top: 0; left: 0; width: 100%; height: 110px; }
  .nav-link { position: absolute; top: 45px; font-family: var(--sans); font-weight: 700; font-size: 10px; color: var(--white); text-transform: uppercase; letter-spacing: .2px; }
  .nav-shop { left: 600px; } .nav-authors { left: 673px; } .nav-explore { left: 766px; } .nav-blog { left: 858px; } .nav-contact { left: 930px; }
  .book-talks { position: absolute; left: 1029px; top: 33px; width: 112px; height: 37px; border: 1.5px solid var(--white); color: var(--gold); font-family: var(--sans); font-weight: 700; font-size: 9px; text-transform: uppercase; display: flex; align-items: center; justify-content: center; }

  /* Hero */
  .hero { position: absolute; left: 0; top: 110px; width: 1200px; height: 680px; background: var(--hero-black); }
  .brand-mark { position: absolute; left: 0; width: 100%; top: 200px; text-align: center; }
  .brand-dot { display: block; width: 34px; height: 34px; border-radius: 50%; background: var(--gold); margin: 0 auto 18px; }
  .brand-name { display: block; font-family: var(--serif); font-size: 52px; color: var(--gold); line-height: 1; }
  .hero-title { position: absolute; left: 0; width: 100%; top: 400px; text-align: center; font-family: var(--serif); font-size: 37px; font-weight: 400; line-height: 1.2; }
  .hero-text { position: absolute; left: 360px; width: 480px; top: 456px; text-align: center; font-size: 19px; line-height: 29px; }
  .slider-dots { position: absolute; display: flex; gap: 8px; }
  .slider-dots span { width: 6px; height: 6px; border-radius: 50%; background: var(--dot-grey); }
  .slider-dots span.active { background: var(--pink); }
  .hero-dots { left: 574px; top: 561px; }
  .social-links { position: absolute; left: 41px; top: 644px; display: flex; gap: 30px; }
  .social-links span { width: 15px; height: 15px; border-radius: 50%; background: var(--pink); }

  .divider { position: absolute; left: 0; width: 1200px; background: var(--divider); }
  .divider-top { top: 790px; height: 10px; }
  .divider-bottom { top: 1575px; height: 8px; }

  /* Collections */
  .collections { position: absolute; left: 0; top: 800px; width: 1200px; height: 775px; background: var(--section-dark); }
  .collections-title { position: absolute; left: 0; width: 100%; top: 86px; text-align: center; font-family: var(--serif); font-weight: 400; font-size: 37px; line-height: 1.2; }
  .category-card { position: absolute; top: 179px; width: 238px; height: 320px; background: var(--pink); display: block; color: var(--white); }
  .product-photo { height: 191px; background: radial-gradient(circle at 50% 50%, #d8d6dc 0%, #f4f4f6 45%, #ffffff 75%); }
  .category-name { display: block; text-align: center; font-family: var(--serif); font-size: 29px; line-height: 1.2; margin-top: 13px; color: var(--white); }
  .card-earring { left: 66px; } .card-bracelets { left: 343px; } .card-rings { left: 620px; } .card-necklaces { left: 896px; }
  .explore-title { position: absolute; left: 0; width: 100%; top: 570px; text-align: center; font-family: var(--serif); font-weight: 400; font-size: 37px; line-height: 1.2; }
  .explore-text { position: absolute; left: 345px; width: 510px; top: 640px; text-align: center; font-size: 12.5px; line-height: 23px; }

  /* Team */
  .team { position: absolute; left: 0; top: 1583px; width: 1200px; height: 767px; background: var(--section-dark); }
  .team-title { position: absolute; left: 97px; top: 265px; font-family: var(--serif); font-weight: 400; font-size: 30px; line-height: 1.2; }
  .team-text { position: absolute; left: 97px; top: 325px; width: 370px; font-size: 12.5px; line-height: 22.5px; }
  .team-tagline { position: absolute; left: 97px; top: 446px; font-size: 12px; font-weight: 700; text-transform: uppercase; }
  .team-tile { position: absolute; width: 198px; height: 199px; background: var(--pink); }
  .team-tile.portrait { background: linear-gradient(160deg, #8a6a4e 0%, #c99a7a 45%, #b3261e 100%); }
  .tile-1 { left: 494px; top: 153px; } .tile-2 { left: 700px; top: 153px; } .tile-3 { left: 906px; top: 153px; }
  .tile-4 { left: 494px; top: 360px; } .tile-5 { left: 700px; top: 360px; } .tile-6 { left: 906px; top: 360px; }
  .team-dots { left: 786px; top: 609px; }
</style>
</head>
<body>
<div class="page">
  <header class="site-header">
    <nav class="main-nav">
      <a class="nav-link nav-shop" href="#">Shop</a>
      <a class="nav-link nav-authors" href="#">Authors</a>
      <a class="nav-link nav-explore" href="#">Explore</a>
      <a class="nav-link nav-blog" href="#">Blog</a>
      <a class="nav-link nav-contact" href="#">Contact</a>
      <a class="book-talks" href="#">Book Talks Now</a>
    </nav>
  </header>

  <section class="hero">
    <div class="brand-mark">
      <span class="brand-dot"></span>
      <span class="brand-name">Bramblewick</span>
    </div>
    <h1 class="hero-title">Bramblewick Jewellery</h1>
    <p class="hero-text">The products are designed to make the wearer not only feel good</p>
    <div class="slider-dots hero-dots"><span class="active"></span><span></span><span></span><span></span></div>
    <div class="social-links" aria-label="Social links"><span></span><span></span><span></span><span></span></div>
  </section>

  <div class="divider divider-top"></div>

  <section class="collections">
    <h2 class="collections-title">All the Jewellery is designed by myself Marjorie Toller</h2>
    <a class="category-card card-earring" href="#"><div class="product-photo" role="img" aria-label="Pair of dark freshwater pearl stud earrings"></div><span class="category-name">Earring</span></a>
    <a class="category-card card-bracelets" href="#"><div class="product-photo" role="img" aria-label="Silver heart pendant filled with white pearls"></div><span class="category-name">Bracelets</span></a>
    <a class="category-card card-rings" href="#"><div class="product-photo" role="img" aria-label="Silver ring with a single pearl"></div><span class="category-name">Rings</span></a>
    <a class="category-card card-necklaces" href="#"><div class="product-photo" role="img" aria-label="Bracelet of dark freshwater pearls"></div><span class="category-name">Necklaces</span></a>
    <h2 class="explore-title">Explore Now</h2>
    <p class="explore-text">Lorem ipsum dolor sit amet, consectetur adipisicing elit, sed do eiusmod tempor incididunt ut ero labore et dolore magna aliqua. Ut enim ad minim veniam, quis nostrud exercitation ullamco.</p>
  </section>

  <div class="divider divider-bottom"></div>

  <section class="team">
    <h2 class="team-title">Our Team.</h2>
    <p class="team-text">Lorem ipsum dolor sit amet, consectetur adipisicing elit, sed do eiusmod tempor incididunt ut ero labore et dolore magna aliqua. Ut enim ad minim veniam, quis nostrud exercitation ullamco poriti laboris nisi ut aliquip ex ea commodo consequat.</p>
    <p class="team-tagline">Lorem ipsum dolor amet consectetuer</p>
    <div class="team-tile portrait tile-1" role="img" aria-label="Portrait photo of the jewellery designer"></div>
    <div class="team-tile tile-2"></div>
    <div class="team-tile tile-3"></div>
    <div class="team-tile tile-4"></div>
    <div class="team-tile tile-5"></div>
    <div class="team-tile tile-6"></div>
    <div class="slider-dots team-dots"><span class="active"></span><span></span><span></span><span></span></div>
  </section>
</div>
</body>
</html>
```